Decals By Marlo needs a website and logo design

I am starting a home business, "Decals By Marlo", which I will sell car decals/decals of some sort. I am looking for a creative and professional looking website. I do not want anything too plain/bland, or else I could design it myself. I am up for many options, when it comes to text/colors, and I am not opposed to much. Just nothing too plain. Currently have no logo design to use, may also add this to the project as well. ( I use Wordpress for my site server so it has to be compatible to be used with that website.
Also, I make decals that mainly go on car windows, not as big on car body’s. Also put decals on glassware, and other items. But mainly car windows

Industry/Entity Type

Business

Coding

Coded - Design and coding required

Font styles to use
Serif
Sans Serif

Requirements
Nice to have
• some color, not be bland and white everywhere.

```html
<!DOCTYPE html>
<html lang="en">
<head>
<meta charset="utf-8">
<title>Decals By Marlo</title>
<link href="https://fonts.googleapis.com/css2?family=Roboto:wght@300;400;500;700&family=Roboto+Condensed:wght@300;400&display=swap" rel="stylesheet">
<style>
:root{
  --blue:#3b67b8;
  --blue-dark:#2c54a0;
  --ink:#1c1c1c;
  --text:#555;
  --muted:#888;
  --line:#dcdcdc;
  --footer:#f1f1f1;
  --white:#fff;
}
*{margin:0;padding:0;box-sizing:border-box}
html,body{width:782px;height:1200px;overflow:hidden;background:var(--white);font-family:'Roboto',sans-serif;color:var(--text)}
a{text-decoration:none}
.page{position:relative;width:782px;height:1200px}

.site-header{position:absolute;left:36px;top:0;width:713px;height:82px}
.brand{position:absolute;left:0;top:26px;display:flex;align-items:center;gap:10px}
.brand-mark{width:34px;height:34px;background:var(--blue);border-radius:4px}
.brand-name{font-weight:700;font-size:23px;color:#6d6d6d;letter-spacing:-.3px}
.utility{position:absolute;right:4px;top:21px;font-size:8px;display:flex;gap:9px;color:var(--ink)}
.utility .wish{color:#bbb}
.social{position:absolute;right:0;top:39px;display:flex;align-items:center;gap:6px}
.social .label{font-size:8px;font-weight:500;color:var(--ink);margin-right:2px}
.social .dot{width:18px;height:18px;border-radius:50%;background:#555}
.social .dot.active{background:var(--blue)}

.main-nav{position:absolute;left:36px;top:82px;width:713px;height:36px;background:var(--blue);border:2px solid #9cb4e0;display:flex;align-items:center;justify-content:space-around;padding:0 8px}
.main-nav a{color:var(--white);font-size:11px;font-weight:500;text-transform:uppercase}

.hero{position:absolute;left:36px;top:118px;width:713px;height:297px;overflow:hidden}
.hero-photo{position:absolute;inset:0;background:linear-gradient(180deg,#3fb6c4 0%,#6cc9cc 28%,#a9d6cf 48%,#dcdcd2 68%,#ece4d6 100%)}
.hero-car{position:absolute;left:0;top:0;width:300px;height:297px;background:
  radial-gradient(ellipse 70% 55% at 45% 55%,#2f8fa6 0%,#2a7c91 40%,rgba(34,92,110,.85) 65%,rgba(60,70,78,0) 100%),
  linear-gradient(180deg,rgba(40,60,70,.55),rgba(30,40,45,.7) 85%,rgba(30,40,45,0))}
.hero-badge{position:absolute;left:422px;top:20px;width:128px;height:104px;border-radius:50%;background:radial-gradient(circle at 50% 52%,#f2d23a 0%,#e9c22b 38%,#5a64a8 60%,#1e2230 78%,rgba(30,34,48,0) 100%)}
.hero-copy{position:absolute;left:300px;top:132px;width:330px;text-align:center;color:var(--ink)}
.hero-copy h1{font-family:'Roboto Condensed',sans-serif;font-weight:400;font-size:29px;line-height:30px;text-transform:uppercase}
.hero-copy p{font-family:'Roboto Condensed',sans-serif;font-weight:300;font-size:15px;margin-top:7px;text-transform:uppercase}
.btn{display:inline-block;background:var(--blue);color:var(--white);font-size:10px;font-weight:500;text-transform:uppercase;border:2px solid #a9c0ea}
.hero-copy .btn{margin-top:11px;padding:8px 16px;font-size:11px}
.hero-arrow{position:absolute;top:125px}

.tile{position:absolute;overflow:hidden}
.tile-photo{position:absolute;inset:0}
.tile-title{position:absolute;left:0;top:0;right:0;height:35px;background:rgba(59,103,184,.92);color:var(--white);font-size:12px;font-weight:500;padding:12px 14px}
.tile-title.dark{background:rgba(40,40,40,.85)}
.tile .btn{position:absolute;right:10px;bottom:8px;padding:6px 10px}

.featured-title{position:absolute;left:0;width:782px;top:778px;text-align:center;font-size:15px;font-weight:500;color:var(--ink)}
.product{position:absolute;top:808px;width:165px;height:168px;border:1px solid var(--line)}
.product-photo{height:90px}
.product-name{font-size:9px;text-align:center;margin-top:12px;line-height:14px;color:var(--text)}
.product .order{display:block;width:65px;margin:8px auto 0;border:1px solid #444;text-align:center;font-size:8px;padding:4px 0;color:var(--ink)}
.product .order.primary{background:var(--blue);color:var(--white);border-color:var(--blue)}

.site-footer{position:absolute;left:0;top:1006px;width:782px;height:157px;background:var(--footer)}
.foot-col{position:absolute;top:22px}
.foot-col h3{font-size:11px;font-weight:400;color:var(--ink);text-transform:uppercase;padding-bottom:5px;border-bottom:1px solid #333;display:inline-block}
.foot-col ul{list-style:none;margin-top:6px}
.foot-col li{font-size:9px;line-height:16.7px;color:var(--text)}
.foot-col li.current{color:var(--blue)}
.newsletter p{font-size:8px;line-height:11px;width:160px;margin-top:6px}
.newsletter .field{width:158px;height:24px;border:1px solid var(--line);background:var(--white);font-size:8px;color:#999;padding:7px 11px;margin-top:6px}
.newsletter .btn{margin-top:5px;padding:6px 16px;border:none}
.copyright{position:absolute;left:0;top:1163px;width:782px;height:37px;background:var(--blue);color:var(--white);font-size:9px;text-align:center;line-height:37px}
</style>
</head>
<body>
<div class="page">

<header class="site-header">
  <div class="brand"><span class="brand-mark"></span><span class="brand-name">Decals By Marlo</span></div>
  <div class="utility"><span>Login</span><span class="wish">View Wishlist (0)</span><span>Checkout</span></div>
  <div class="social"><span class="label">GET CONNETED</span><span class="dot active"></span><span class="dot"></span><span class="dot"></span><span class="dot"></span><span class="dot"></span><span class="dot"></span></div>
</header>

<nav class="main-nav">
  <a href="#">Home</a><a href="#">About us</a><a href="#">Car Decals</a><a href="#">Installation Instructions</a><a href="#">Customer Gallery</a><a href="#">Vinyl Material</a><a href="#">Contact us</a>
</nav>

<section class="hero">
  <div class="hero-photo" role="img" aria-label="Beach shoreline with the sea behind"></div>
  <div class="hero-car" role="img" aria-label="Rear of a teal car with a round decal on its back window"></div>
  <div class="hero-badge" role="img" aria-label="Round charity ride decal in yellow and navy"></div>
  <div class="hero-copy">
    <h1>Car Decals<br>Decals of some sort</h1>
    <p>Perfect way to advertise for your business</p>
    <a class="btn" href="#">Shop Now</a>
  </div>
  <svg class="hero-arrow" style="left:12px" width="22" height="46" viewBox="0 0 22 46"><path d="M20 2 L3 23 L20 44" fill="none" stroke="#fff" stroke-width="2.5"/></svg>
  <svg class="hero-arrow" style="right:10px" width="22" height="46" viewBox="0 0 22 46"><path d="M2 2 L19 23 L2 44" fill="none" stroke="#2c54a0" stroke-width="2.5"/></svg>
</section>

<div class="tile" style="left:36px;top:444px;width:225px;height:306px">
  <div class="tile-photo" role="img" aria-label="Silver car door with an eagle and flag decal" style="background:radial-gradient(ellipse 45% 35% at 62% 30%,#8e7a62 0%,#b9b3a8 55%,rgba(220,225,232,0) 100%),radial-gradient(ellipse 40% 40% at 10% 78%,#3a3e44 0%,#8d939b 55%,rgba(200,205,212,0) 100%),linear-gradient(135deg,#eef0f3,#d3d8df 60%,#b3b9c2)"></div>
  <div class="tile-title">Car Decals</div>
  <a class="btn" href="#">Shop Now</a>
</div>
<div class="tile" style="left:280px;top:444px;width:225px;height:148px">
  <div class="tile-photo" role="img" aria-label="Black sports car with red stripe decal" style="background:radial-gradient(ellipse 50% 18% at 45% 60%,#b8323a 0%,rgba(120,30,35,.6) 55%,rgba(30,30,30,0) 100%),linear-gradient(180deg,#9a9a9a 20%,#3a3a3a 50%,#141414 85%)"></div>
  <div class="tile-title dark">Car Decals</div>
  <a class="btn" href="#">Shop Now</a>
</div>
<div class="tile" style="left:280px;top:603px;width:225px;height:148px">
  <div class="tile-photo" role="img" aria-label="Green convertible with yellow star decals" style="background:radial-gradient(ellipse 35% 20% at 45% 66%,#d9cf3f 0%,rgba(200,190,60,.4) 50%,rgba(40,80,60,0) 100%),linear-gradient(180deg,#708a66 20%,#3d6b56 45%,#2a4f43 70%,#a8aca8 95%)"></div>
  <div class="tile-title dark">Car Decals</div>
  <a class="btn" href="#">Shop Now</a>
</div>
<div class="tile" style="left:523px;top:444px;width:226px;height:306px">
  <div class="tile-photo" role="img" aria-label="White car hood with a black rose outline decal" style="background:radial-gradient(ellipse 42% 26% at 50% 47%,#b9b9b9 0%,#e4e4e4 50%,rgba(240,240,240,0) 100%),linear-gradient(180deg,#3a3c40 12%,#d9dbde 28%,#f4f4f4 55%,#2a2a2a 72%,#454545 80%,#ececec 92%)"></div>
  <div class="tile-title">Car Decals</div>
  <a class="btn" href="#">Shop Now</a>
</div>

<h2 class="featured-title">FEATURED PRODUCTS</h2>

<div class="product" style="left:36px">
  <div class="product-photo" role="img" aria-label="White hatchback with orange graphic decal" style="background:radial-gradient(ellipse 35% 30% at 78% 55%,#e0894a 0%,rgba(220,140,80,.3) 60%,rgba(230,230,230,0) 100%),linear-gradient(180deg,#8c9280,#d9dcdd 45%,#ededed 80%,#8a8a8a)"></div>
  <p class="product-name">Car Decals / Stickers (Opaque)<br>1' x 1' Starts at Rs190</p>
  <a class="order primary" href="#">Start Order</a>
</div>
<div class="product" style="left:219px">
  <div class="product-photo" role="img" aria-label="White car with blue company livery" style="background:radial-gradient(ellipse 30% 14% at 50% 58%,#3a78c4 0%,rgba(60,120,196,.3) 60%,rgba(240,240,240,0) 100%),radial-gradient(ellipse 48% 32% at 50% 58%,#f2f2f2 0%,#d5d8de 60%,rgba(20,20,20,0) 100%),#141414"></div>
  <p class="product-name">Car Decals / Stickers (Opaque)<br>1' x 1' Starts at Rs190</p>
  <a class="order" href="#">Start Order</a>
</div>
<div class="product" style="left:402px">
  <div class="product-photo" role="img" aria-label="Dark sedan with orange sponsor wrap" style="background:radial-gradient(ellipse 45% 25% at 55% 58%,#d2622a 0%,#8a3c24 50%,rgba(40,50,65,0) 100%),linear-gradient(180deg,#b5b5b5 10%,#2e3a4a 40%,#253040 75%,#a3a3a3)"></div>
  <p class="product-name">Car Decals / Stickers (Opaque)<br>1' x 1' Starts at Rs190</p>
  <a class="order" href="#">Start Order</a>
</div>
<div class="product" style="left:585px">
  <div class="product-photo" role="img" aria-label="White patrol car with gold security lettering" style="background:radial-gradient(ellipse 22% 14% at 45% 60%,#c9a545 0%,rgba(200,165,70,.3) 60%,rgba(240,240,240,0) 100%),radial-gradient(ellipse 50% 30% at 50% 58%,#f3f3f3 0%,#dcdcdc 60%,rgba(60,70,50,0) 100%),linear-gradient(180deg,#4a5a3a,#5b6650 50%,#2a2a2a)"></div>
  <p class="product-name">Car Decals / Stickers (Opaque)<br>1' x 1' Starts at Rs190</p>
  <a class="order" href="#">Start Order</a>
</div>

<footer class="site-footer">
  <div class="foot-col" style="left:36px">
    <h3>Nevigation</h3>
    <ul><li class="current">Home</li><li>About us</li><li>Car Decals</li><li>Instalation Instructions</li><li>Customer Gallery</li><li>Contacts</li></ul>
  </div>
  <div class="foot-col" style="left:218px">
    <h3>My Account</h3>
    <ul><li>My Account</li><li>My Credit slips</li><li>My products returns</li><li>My Personal info</li><li>My Addresses</li><li>Vinyl Materials</li></ul>
  </div>
  <div class="foot-col" style="left:414px">
    <h3>Decals</h3>
    <ul><li>Car Sticker</li><li>Decals</li><li>Car Decals</li><li>Auto Decals</li><li>Top Decals</li><li>Wall Decals</li></ul>
  </div>
  <div class="foot-col newsletter" style="left:590px">
    <h3>Newsletter</h3>
    <p>Add you e-mail addres to our newsletter to be always on time with all promotions.</p>
    <div class="field">E-mail address</div>
    <a class="btn" href="#">Submit</a>
  </div>
</footer>
<div class="copyright">Copyright © 2017 Decals By Marlo. All rights reserved.</div>

</div>
</body>
</html>
```